Business Card Design Project

Attached is a rough business card design. We like this general design but we feel that the layout, text, color can use improvement and we seek the help of a professional designer.
We have a television and film production company based in New York. We need our cards for television network executives, other production executives, financiers etc. We deal with creative types as well as business people so we need the card to be interesting and edgy just like the name of our company - KICKTHEDOOR. The design should reflect the edgy, punk rock attitude of our company.
We prefer orange typeface for the logo but we're open to other ideas. I am attaching our existing business card and other files to help with the design.
Thank you in advance!!
Updates
Target Market(s)
Television and film producers, television network executives, other production executives, financiers, distribution companies
Industry/Entity Type
Film Production
Requirements
Must have
- I am attaching a photo of the company mascot which is a dog. We prefer to have the dog's photo as part of the card but we're open to the other ideas.
Name, phone number, email

```html
<!DOCTYPE html>
<html lang="en">
<head>
<meta charset="utf-8">
<title>KICKTHEDOOR – Business Card</title>
<link rel="stylesheet" href="https://fonts.googleapis.com/css2?family=Ubuntu:wght@300;400&display=swap">
<style>
  :root {
    --page-bg: #e6e2dc;
    --card-dark: #1c1b1f;
    --card-dark-edge: #2b2a30;
    --accent-orange: #e8a33c;
    --text-warm: #e7c79a;
    --photo-light: #efe6dd;
    --photo-mid: #c9a583;
    --photo-deep: #6b4a35;
  }
  * { margin: 0; padding: 0; box-sizing: border-box; }
  html, body {
    width: 1200px;
    height: 912px;
    overflow: hidden;
    background: var(--page-bg);
  }
  .canvas {
    width: 1200px;
    height: 912px;
    display: flex;
    align-items: center;
    justify-content: center;
  }
  .business-card {
    width: 960px;
    height: 548px;
    border-radius: 34px;
    overflow: hidden;
    display: flex;
    box-shadow: 0 18px 40px rgba(0, 0, 0, 0.25);
  }
  .card-info {
    flex: 0 0 56%;
    display: flex;
    flex-direction: column;
    justify-content: space-between;
    padding: 60px 64px 58px;
    background: linear-gradient(160deg, var(--card-dark-edge) 0%, var(--card-dark) 55%);
    font-family: "Ubuntu", sans-serif;
  }
  .brand-name {
    display: flex;
    align-items: center;
    gap: 14px;
    font-size: 30px;
    font-weight: 400;
    letter-spacing: 4px;
    color: var(--accent-orange);
    line-height: 1;
  }
  .brand-mark {
    width: 14px;
    height: 14px;
    background: var(--accent-orange);
    flex: none;
  }
  .contact { color: var(--text-warm); }
  .contact-name {
    font-size: 34px;
    font-weight: 400;
    margin-bottom: 14px;
  }
  .contact-line {
    font-size: 23px;
    font-weight: 300;
    line-height: 1.45;
  }
  .card-photo {
    flex: 1;
    background:
      radial-gradient(ellipse at 60% 45%, var(--photo-mid) 0%, rgba(201,165,131,0) 60%),
      linear-gradient(200deg, var(--photo-light) 0%, var(--photo-mid) 60%, var(--photo-deep) 100%);
  }
</style>
</head>
<body>
  <main class="canvas">
    <article class="business-card">
      <section class="card-info">
        <div class="brand-name"><span class="brand-mark"></span>KICKTHEDOOR</div>
        <div class="contact">
          <p class="contact-name">Dana Whitfield</p>
          <p class="contact-line">917-555-0184</p>
          <p class="contact-line">dana@kickthedoor.com</p>
          <p class="contact-line">www.kickthedoor.com</p>
        </div>
      </section>
      <div class="card-photo" role="img" aria-label="Photo of the company mascot, a fawn bulldog, in warm soft light"></div>
    </article>
  </main>
</body>
</html>
```